Guided Study Tour - Halmerfest Leipzig Two Sided Flyer

We need a two-sided flyer for a Guided Study Tour to Halmerfest Leipzig. We want beautiful pictures of Germany and if possible some of the Halmer venues our participants will be visiting. I have also provided the content that needs to be included. Also, in the attached document I provided a link to the Halmerfest event. Please read and watch the video to be inspired.
This flyer should be beautiful and engaging. It needs to grab your attention right away and really highlight the wonderful things that they will be doing and that are included in the tour. This is a once in a lifetime opportunity for people to experience. We are targeting Music Directors and Music professionals.
Both attached logos need to be present on the flyer.

```html
<!DOCTYPE html>
<html lang="en">
<head>
<meta charset="utf-8">
<title>Guided Study Tour – Halmerfest Leipzig Flyer</title>
<link rel="stylesheet" href="https://fonts.googleapis.com/css2?family=Montserrat:wght@400;500;600;700;800&family=Oswald:wght@500;600&display=swap">
<style>
:root{
  --stage:#5b5b5b;
  --blue:#1f63d0;
  --red:#d61f2b;
  --red-bright:#ec1c24;
  --white:#ffffff;
  --ink-blue:#1d5cc2;
  --ink:#1b1b2a;
}
*{box-sizing:border-box;margin:0;padding:0}
html,body{width:1200px;height:1200px;overflow:hidden}
body{background:var(--stage);font-family:"Montserrat",sans-serif;position:relative}
.page{position:absolute;top:278px;width:458px;height:644px;background:var(--white);overflow:hidden;box-shadow:0 4px 14px rgba(0,0,0,.35)}
.page--front{left:106px}
.page--back{left:636px}
.page__bg{position:absolute;inset:0;width:458px;height:644px}
.abs{position:absolute}
.brand{display:flex;align-items:center;gap:8px;font-weight:700;color:var(--red)}
.brand__dot{width:34px;height:34px;border-radius:50%;background:var(--red)}
.brand__name{font-size:22px;line-height:1}
.brand--small .brand__dot{width:26px;height:26px}
.brand--small .brand__name{font-size:17px}
.partner{display:flex;align-items:center;gap:6px;font-weight:700;color:var(--ink-blue);font-size:14px;line-height:16px}
.partner__dot{width:14px;height:14px;border-radius:50%;background:var(--ink-blue)}
.front-date{top:260px;left:0;width:458px;text-align:center;color:var(--white);font-weight:800;font-size:22px;line-height:24px}
.front-title{top:283px;left:0;width:458px;text-align:center;color:var(--white);font-family:"Oswald",sans-serif;font-weight:600;font-size:28px;line-height:32px}
.front-place{top:322px;left:0;width:458px;text-align:center;color:var(--white);font-weight:700;font-size:14px;line-height:16px}
.front-sub{top:339px;left:0;width:458px;text-align:center;color:var(--white);font-size:13.3px;line-height:16px}
.pill{top:366px;left:38px;width:382px;height:27px;border-radius:14px;background:var(--red);color:var(--white);font-family:"Oswald",sans-serif;font-weight:500;font-size:14px;display:flex;align-items:center;justify-content:center}
.photo-circle{position:absolute;border-radius:50%;border:5px solid var(--red);box-shadow:0 0 0 3px var(--white)}
.call{right:20px;text-align:right;color:var(--white)}
.call__label{font-weight:600;font-size:15px;line-height:18px}
.call__number{font-weight:700;font-size:27px;line-height:30px}
.hl-title{top:16px;left:18px;color:var(--ink-blue);font-weight:800;font-size:21px;line-height:24px}
.hl-list{top:40px;left:18px;list-style:none}
.hl-list li{display:flex;align-items:center;gap:8px;height:27px;font-size:12.5px;font-weight:500;color:var(--ink)}
.hl-list li svg{flex:none}
.block-title{color:var(--white);font-weight:700;font-size:15.5px;line-height:18px}
.block-text{color:var(--white);font-size:8.8px;line-height:10.5px;font-weight:500}
.performers{top:229px;left:18px;width:218px}
.performers p{margin-top:5px}
.study{top:299px;left:18px;width:218px}
.study ul{list-style:none;margin-top:3px}
.study li{margin-bottom:6px}
.quote{top:214px;left:239px;width:201px;height:148px;border-radius:12px;background:var(--red-bright);color:var(--white);padding:8px 7px}
.quote__label{font-weight:700;font-size:14px;line-height:16px}
.quote__text{font-size:11.5px;line-height:14px;margin-top:6px;text-align:justify;font-weight:500}
.quote__by{font-size:10.5px;margin-top:6px;line-height:13px;font-weight:500}
</style>
</head>
<body>

<section class="page page--front">
  <svg class="page__bg" viewBox="0 0 458 644" aria-hidden="true">
    <defs>
      <linearGradient id="blueFront" x1="0" y1="0" x2="1" y2="1">
        <stop offset="0" stop-color="#1a56c2"/><stop offset="1" stop-color="#2a78e3"/>
      </linearGradient>
      <linearGradient id="cityFront" x1="0" y1="0" x2="0" y2="1">
        <stop offset="0" stop-color="#8fc0ea"/><stop offset=".45" stop-color="#c9b79a"/><stop offset="1" stop-color="#8a6c55"/>
      </linearGradient>
    </defs>
    <rect width="458" height="644" fill="url(#blueFront)"/>
    <path d="M0,0 H458 V212 C380,218 300,256 190,262 C110,266 40,236 0,204 Z" fill="var(--red)"/>
    <path role="img" aria-label="Aerial photo of a German city skyline along a river with a TV tower" d="M0,0 H458 V200 C380,206 300,246 190,250 C110,254 40,222 0,188 Z" fill="url(#cityFront)"/>
    <path d="M0,500 C120,575 300,560 458,498 V644 H0 Z" fill="var(--red)"/>
    <path d="M0,496 C140,560 300,552 458,512 V644 H0 Z" fill="var(--white)"/>
    <path d="M158,644 C200,598 300,560 458,552 V644 Z" fill="url(#blueFront)"/>
  </svg>

  <div class="abs brand" style="top:18px;left:18px"><span class="brand__dot"></span><span class="brand__name">Marlow Tours</span></div>

  <p class="abs front-date">JUNE 12-16, 2019</p>
  <h1 class="abs front-title">GUIDED STUDY TOUR – HALMERFEST</h1>
  <p class="abs front-place">LEIPZIG, GERMANY</p>
  <p class="abs front-sub">Plusday trip to Dresden and full day and overnight in Prague</p>
  <p class="abs pill">JOIN US FOR A ONCE IN A LIFETIME .... LED BY DANIEL REEVE....</p>

  <div class="photo-circle" role="img" aria-label="Photo of a hilltop castle in front of alpine mountains" style="left:24px;top:416px;width:124px;height:124px;background:linear-gradient(180deg,#7fb2e0,#9ab7a8 55%,#3f7a3a)"></div>
  <div class="photo-circle" role="img" aria-label="Photo of a composer statue in front of a Gothic church" style="left:167px;top:416px;width:124px;height:124px;background:linear-gradient(180deg,#5f9a3f,#a9a394 55%,#7d7568)"></div>
  <div class="photo-circle" role="img" aria-label="Photo of a cathedral and riverfront lit up at dusk" style="left:309px;top:416px;width:124px;height:124px;background:linear-gradient(180deg,#2d3a8f,#7a5ea8 55%,#c98a3a)"></div>

  <div class="abs partner" style="top:596px;left:18px"><span class="partner__dot"></span>Heritage Chorale Tours</div>

  <div class="abs call" style="top:584px">
    <p class="call__label">Call us today:</p>
    <p class="call__number">800.555.0142</p>
  </div>
</section>

<section class="page page--back">
  <svg class="page__bg" viewBox="0 0 458 644" aria-hidden="true">
    <defs>
      <linearGradient id="blueBack" x1="0" y1="0" x2="1" y2="1">
        <stop offset="0" stop-color="#1a56c2"/><stop offset="1" stop-color="#2a78e3"/>
      </linearGradient>
      <linearGradient id="fadeCity" x1="0" y1="0" x2="0" y2="1">
        <stop offset="0" stop-color="#e9ecf6"/><stop offset="1" stop-color="#f3eee6"/>
      </linearGradient>
    </defs>
    <rect width="458" height="644" fill="url(#blueBack)"/>
    <rect role="img" aria-label="Faded photo of a cathedral skyline" width="458" height="230" fill="url(#fadeCity)"/>
    <path d="M0,132 C30,196 110,222 220,216 C320,212 380,170 458,156 V0 H0 Z" fill="var(--red)"/>
    <path d="M0,122 C30,184 110,210 220,204 C320,198 380,158 458,146 V0 H0 Z" fill="url(#fadeCity)"/>
    <path d="M0,510 C80,482 180,478 290,484 C360,488 420,474 458,452 V644 H0 Z" fill="var(--red)"/>
    <path d="M0,520 C80,494 180,490 290,496 C360,500 420,486 458,464 V644 H0 Z" fill="var(--white)"/>
    <path d="M164,644 C210,600 320,560 458,546 V644 Z" fill="url(#blueBack)"/>
  </svg>

  <h2 class="abs hl-title">HALMERFEST HIGHLIGHTS:</h2>
  <ul class="abs hl-list">
    <li><svg width="11" height="11" viewBox="0 0 11 11"><circle cx="5.5" cy="5.5" r="5.5" fill="var(--ink-blue)"/><path d="M4.3,3 L6.8,5.5 L4.3,8" stroke="#fff" stroke-width="1.4" fill="none"/></svg>More than 100 Concerts in 42 different Halmer venues</li>
    <li><svg width="11" height="11" viewBox="0 0 11 11"><circle cx="5.5" cy="5.5" r="5.5" fill="var(--ink-blue)"/><path d="M4.3,3 L6.8,5.5 L4.3,8" stroke="#fff" stroke-width="1.4" fill="none"/></svg>World Class Musicians &amp; Celebrated Recording Artists</li>
    <li><svg width="11" height="11" viewBox="0 0 11 11"><circle cx="5.5" cy="5.5" r="5.5" fill="var(--ink-blue)"/><path d="M4.3,3 L6.8,5.5 L4.3,8" stroke="#fff" stroke-width="1.4" fill="none"/></svg>Day trips to Weimer &amp; Dresden</li>
    <li><svg width="11" height="11" viewBox="0 0 11 11"><circle cx="5.5" cy="5.5" r="5.5" fill="var(--ink-blue)"/><path d="M4.3,3 L6.8,5.5 L4.3,8" stroke="#fff" stroke-width="1.4" fill="none"/></svg>Bilingual pre-concert talks &amp; lectures with Halmer Scholars</li>
  </ul>

  <div class="abs performers">
    <h3 class="block-title">Featured Performers:</h3>
    <p class="block-text">Jonas Vallé, Tomas Keller, Cantaro, Leipzig</p>
    <p class="block-text">Lindenhall Orchestra, Vellora,&amp; the Leipzig Nikolaichor</p>
  </div>

  <div class="abs study">
    <h3 class="block-title">Study Tour Highlights:</h3>
    <ul class="block-text">
      <li>Access to dress rehearsals</li>
      <li>Meet the artist opportunities</li>
      <li>Post-concert discussions led by Daniel Reeve</li>
      <li>Study sessions on Halmer's B-Minor Mass, Magnificat,</li>
      <li>St. John Passion, St. Matthew Passion &amp; Weimar Cantatashours</li>
      <li>Guidance in planning individual concert itinerary</li>
      <li>Professional development or continuing education credit</li>
    </ul>
  </div>

  <aside class="abs quote">
    <p class="quote__label">Quote:</p>
    <p class="quote__text">“This is where it all has begun...- this is why our guests have tears in their eyes listening to the St. Matthew Passion or the B-Minor Mass”</p>
    <p class="quote__by">~ Martin Kessel, Musicologist, Festival Director</p>
  </aside>

  <div class="photo-circle" role="img" aria-label="Photo of a grand town hall with a tower under a blue sky" style="left:256px;top:378px;width:168px;height:168px;background:linear-gradient(180deg,#2f6fc4,#9fb7d6 45%,#c8b9a0 70%,#6e8a3e)"></div>

  <div class="abs brand brand--small" style="top:536px;left:18px"><span class="brand__dot"></span><span class="brand__name">Marlow Tours</span></div>
  <div class="abs partner" style="top:584px;left:20px"><span class="partner__dot"></span>Heritage Chorale Tours</div>

  <div class="abs call" style="top:586px">
    <p class="call__label">Call us today:</p>
    <p class="call__number">800.555.0142</p>
  </div>
</section>

</body>
</html>
```